Real Estate Agency Chatterlane Cover Photo

We need a Chatterlane cover photo created for our Real Estate Business. We also need this cover photo adapted to several other platforms. Please read this brindlo doc for full specifications of the job https://files.brindlo-example.net/sheet/d/8QwerPLm4ZxVb2NnKs7RtYhUe3_gHdjAoFcWsMvBn/view?mode=share

Please also carefully read the Must Haves/Should Not Haves

Please contact me if you have any queries. Looking forward to seeing your designs!

Owen

Industry/Entity Type

Real Estate Agent

Requirements
Must have
• The Taglines 'More Money In Your Pocket' and sub tagline 'With Our Low Flat Fee To Sell Your Home'

It can then also have other elements e.g our logo, contact details and anything else you think will work well.

It must also have great graphic design work which looks custom and very clean/modern
Should not have
• Must not have poor quality stock images or anything tacky regarding money etc

```html
<!DOCTYPE html>
<html lang="en">
<head>
<meta charset="utf-8">
<title>NORVA – Cover</title>
<link href="https://fonts.googleapis.com/css2?family=Lato:wght@400;700;900&display=swap" rel="stylesheet">
<style>
  :root {
    --ink: #0e0e0e;
    --brand-red: #e2262b;
    --white: #ffffff;
    --photo-dark: #1f1f1f;
    --photo-mid: #4a4a4a;
    --photo-light: #7a7a7a;
  }
  * { margin: 0; padding: 0; box-sizing: border-box; }
  html, body { width: 1200px; height: 455px; overflow: hidden; background: var(--ink); }
  .cover {
    position: relative;
    width: 1200px;
    height: 455px;
    overflow: hidden;
    font-family: "Lato", Arial, sans-serif;
    color: var(--white);
  }
  .cover__scene {
    position: absolute;
    inset: 0;
    background:
      radial-gradient(ellipse at 70% 85%, rgba(150,150,150,0.55), rgba(0,0,0,0) 55%),
      radial-gradient(ellipse at 18% 60%, rgba(110,110,110,0.45), rgba(0,0,0,0) 45%),
      linear-gradient(180deg, var(--photo-dark) 0%, var(--photo-mid) 60%, var(--photo-light) 100%);
  }
  .cover__shade {
    position: absolute;
    inset: 0;
    background: rgba(0,0,0,0.35);
  }
  .top-band {
    position: absolute;
    left: 0; top: 0;
    width: 1200px; height: 92px;
  }
  .brand {
    position: absolute;
    left: 21px; top: 22px;
    font-weight: 700;
    font-size: 40px;
    letter-spacing: 2px;
    color: var(--brand-red);
    line-height: 1;
  }
  .perks {
    position: absolute;
    top: 23px;
    right: 16px;
    display: flex;
    align-items: center;
    list-style: none;
  }
  .perk {
    display: flex;
    align-items: center;
    margin-left: 16px;
    font-weight: 700;
    font-size: 19px;
    letter-spacing: 0.3px;
    text-transform: uppercase;
  }
  .perk svg { width: 42px; height: 42px; margin-right: 12px; flex: none; }
  .perk--red { color: var(--brand-red); }
  .perk--white { color: var(--white); }
  .headline {
    position: absolute;
    left: 0; right: 0;
    top: 172px;
    text-align: center;
    font-weight: 400;
    font-size: 50px;
    letter-spacing: 2.5px;
    text-transform: uppercase;
    line-height: 1;
  }
  .subline {
    position: absolute;
    left: 0; right: 0;
    top: 271px;
    text-align: center;
    font-weight: 700;
    font-size: 31px;
    letter-spacing: 0.8px;
    line-height: 1;
  }
</style>
</head>
<body>
<main class="cover">
  <div class="cover__scene" role="img" aria-label="Black and white photo of a smiling family relaxing together on a sofa in a bright living room"></div>
  <div class="cover__shade"></div>

  <svg class="top-band" viewBox="0 0 1200 92" preserveAspectRatio="none" aria-hidden="true">
    <polygon fill="#0e0e0e" points="0,0 1200,0 1200,80 1180,76 1160,83 1138,77 1115,84 1092,78 1070,82 1046,75 1020,83 996,78 972,85 948,77 925,81 900,75 876,83 850,78 826,84 800,76 776,82 752,77 728,85 704,78 680,82 655,75 630,83 606,79 582,86 558,77 534,82 510,76 486,84 462,78 438,83 414,76 390,82 366,78 342,85 318,77 294,82 270,75 246,83 222,79 198,84 174,76 150,82 126,78 102,85 78,77 54,82 30,76 12,83 0,78"/>
  </svg>

  <div class="brand">NORVA</div>

  <ul class="perks">
    <li class="perk perk--red">
      <svg viewBox="0 0 42 42" aria-hidden="true">
        <circle cx="21" cy="21" r="20" fill="var(--brand-red)"/>
        <circle cx="21" cy="21" r="13" fill="none" stroke="#fff" stroke-width="2"/>
        <text x="21" y="25" text-anchor="middle" font-family="Lato, sans-serif" font-weight="900" font-size="11" fill="#fff">%</text>
        <line x1="12" y1="12" x2="30" y2="30" stroke="#fff" stroke-width="2.4"/>
      </svg>
      No Commission
    </li>
    <li class="perk perk--white">
      <svg viewBox="0 0 42 42" aria-hidden="true">
        <circle cx="21" cy="21" r="20" fill="var(--white)"/>
        <circle cx="21" cy="21" r="16" fill="var(--brand-red)"/>
        <circle cx="21" cy="17" r="6" fill="none" stroke="#fff" stroke-width="2"/>
        <path d="M21 24 v8 M17 28 l4 4 l4 -4" fill="none" stroke="#fff" stroke-width="2" stroke-linecap="round" stroke-linejoin="round"/>
      </svg>
      Low Flat Fee
    </li>
    <li class="perk perk--red">
      <svg viewBox="0 0 42 42" aria-hidden="true">
        <circle cx="21" cy="21" r="20" fill="var(--brand-red)"/>
        <circle cx="21" cy="21" r="13" fill="none" stroke="#fff" stroke-width="2"/>
        <text x="21" y="26" text-anchor="middle" font-family="Lato, sans-serif" font-weight="900" font-size="14" fill="#fff">$</text>
      </svg>
      Best Selling Price
    </li>
  </ul>

  <h1 class="headline">More Money In Your Pocket</h1>
  <p class="subline">With our Low Flat Fee To Sell Your Home</p>
</main>
</body>
</html>
```